Corvelle Solutions needs an IT Managed Services Website and the logo needs to be updated

We need a new website for our 25 year old IT Managed Services Company. Our company specializes in listening to and understanding our customer needs and goals. Our customers include SME's and Corporates in industries ranging from Medical, Legal, Industrial & Manufacturing and Financial. The services that we offer include: Managed IT Services, Remote Monitoring and Management and Virtualisation. Corvelle Solutions takes technology and makes the lives of our customers easier by applying it appropriately. In the same way, we want a website that is as pleasing to the eye, as it is simple to find information and call to action. The website should say as much in design as it does in content and it should be saying that Corvelle Solutions is your technology partner that listens to you, understands you, delivers solutions and is loyal in our relationship with you. Aesthetically, we want to go for something a little warmer than blue and white, but want to err on the side of professional.
The Logo: We need the "computer" and "ltd" to be removed from the logo. We want to keep the @ on the "u". We would like to freshen up the logo inline with the website design in terms of look and feel and colour.

Target Market(s)

Businesses that require IT Managed Services

Logo Text

Corvelle Solutions

Coding

Coded - Design and coding required

Number of Pages Required

5+ page

Font styles to use
Sans Serif

Colors

Designer to choose colors to be used in the design.

Requirements
Must have
• Each page must have a call to action.

```html
<!DOCTYPE html>
<html lang="en">
<head>
<meta charset="utf-8">
<title>Corvelle Solutions – IT Managed Services</title>
<link rel="stylesheet" href="https://fonts.googleapis.com/css2?family=Montserrat:wght@500;600;700&family=Lato:wght@400;700&display=swap">
<style>
:root{
  --orange:#f7931e;
  --orange-deep:#f26f21;
  --amber:#fbb514;
  --ink:#1f1f1f;
  --body:#333333;
  --grey-band:#4b4847;
  --white:#ffffff;
  --rule:#d6d6d6;
}
*{margin:0;padding:0;box-sizing:border-box}
html,body{width:1200px;height:3279px;overflow:hidden}
body{position:relative;background:var(--white);font-family:"Lato",sans-serif;color:var(--body)}
.abs{position:absolute}
h1,h2,h3,.nav a,.btn,.brand{font-family:"Montserrat",sans-serif}

/* header */
.topbar{left:0;top:0;width:1200px;height:83px;background:var(--orange)}
.nav{position:absolute;top:0;height:83px;display:flex;align-items:center;gap:46px}
.nav a{color:var(--white);text-decoration:none;font-size:15px;font-weight:600;letter-spacing:.3px}
.nav.left{left:98px}
.nav.right{left:810px}
.tab{left:0;top:0}
.brand{color:var(--orange-deep);font-weight:700;white-space:nowrap;text-align:center;line-height:1.1}
.brand small{display:block;font-size:.34em;color:var(--orange-deep);font-weight:700;letter-spacing:.5px}
.brand-top{left:500px;top:12px;width:200px;font-size:36px}

/* hero */
.hero{left:0;top:83px;width:1200px;height:514px;background:linear-gradient(100deg,#5b6068 0%,#8a8f94 35%,#6e7278 60%,#2c2f35 100%)}
.hero-art{left:610px;top:83px;width:560px;height:514px;background:radial-gradient(circle at 50% 48%,rgba(255,255,255,.55) 0 14%,rgba(255,255,255,.15) 30%,rgba(0,0,0,0) 60%)}
.hero-title{left:98px;top:172px;font-size:68px;line-height:82px;color:var(--white);font-weight:700;letter-spacing:1px}
.hero-quote{left:98px;top:286px;font-family:"Montserrat",sans-serif;font-size:26px;color:var(--white);font-weight:600}
.hero-sub{left:98px;top:336px;width:520px;font-size:16px;color:var(--white);line-height:22px}
.chev{top:315px}

.btn{display:flex;align-items:center;justify-content:center;border-radius:24px;font-weight:700;font-size:15px;text-decoration:none}
.btn-amber{background:var(--amber);color:var(--white);box-shadow:0 3px 6px rgba(0,0,0,.25);width:120px;height:44px}
.btn-ghost{border:2px solid var(--white);color:var(--white);width:154px;height:48px}
.btn-ghost.fill{background:var(--amber);border-color:var(--amber)}

/* welcome */
.welcome-kicker{left:98px;top:692px;font-size:34px;color:var(--ink);font-weight:600}
.welcome-title{left:98px;top:735px;font-size:54px;color:var(--orange);font-weight:700}
.welcome-copy{left:98px;top:826px;width:530px;font-size:14px;line-height:22.5px;text-align:justify}
.frame{left:754px;top:675px;width:346px;height:383px;border:3px solid #9a9a9a}
.photo-team{left:717px;top:700px;width:350px;height:375px;background:linear-gradient(135deg,#c9b79a,#8c8378 50%,#5f6a74)}

/* services */
.services{left:0;top:1165px;width:1200px;height:665px;background:radial-gradient(circle at 20% 30%,#5a5756,var(--grey-band) 60%)}
.services-title{left:0;top:1232px;width:1200px;text-align:center;color:var(--white);font-size:48px;line-height:60px;font-weight:700}
.rule-w{height:3px;background:var(--white)}
.svc{top:1371px;width:360px;text-align:center;color:var(--white)}
.svc .icon{width:118px;height:118px;border-radius:50%;border:3px solid var(--white);margin:0 auto;display:flex;align-items:center;justify-content:center}
.svc .icon.hot{background:var(--amber);border-color:var(--white)}
.svc h3{margin-top:36px;font-size:19px;line-height:26px;font-weight:600;white-space:nowrap}
.svc .bar{width:70px;height:2px;background:var(--white);margin:16px auto 20px}
.svc p{font-size:13px;line-height:22px;width:330px;margin:0 auto;height:92px}
.svc .btn{margin:33px auto 0}

/* why */
.why-art{left:0;top:1830px;width:547px;height:588px;background:radial-gradient(circle at 30% 48%,#3c6fa8 0 16%,#9cc8ee 22%,#e9eef3 48%,#ffffff 70%)}
.why-kicker{left:573px;top:1915px;font-size:27px;color:var(--ink);font-weight:600}
.why-title{left:573px;top:1952px;font-size:50px;color:var(--orange);font-weight:700}
.why-copy{left:573px;top:2040px;width:528px;font-size:13.5px;line-height:22.5px}
.why-copy p{margin-bottom:8px}

/* engineers */
.eng{left:0;top:2418px;width:1200px;height:428px;background:linear-gradient(90deg,#dde9ee 0%,#e7eff2 45%,#cfdde4 70%,#9fb8c6 100%)}
.eng-art{left:690px;top:2418px;width:510px;height:428px;background:radial-gradient(circle at 55% 50%,rgba(255,255,255,.9) 0 10%,rgba(170,200,215,.6) 30%,rgba(120,150,170,0) 65%)}
.eng-copy{left:98px;top:2528px;width:558px;font-size:14px;line-height:22.5px;text-align:justify}
.eng-copy p{margin-bottom:22px}

/* footer */
.brand-foot{left:450px;top:2930px;width:300px;font-size:44px}
.social{left:496px;top:3047px;display:flex;gap:12px}
.social span{width:40px;height:40px;border:2.5px solid var(--ink);border-radius:50%}
.foot-nav{left:0;top:3136px;width:1200px;display:flex;justify-content:center;gap:30px;font-family:"Montserrat",sans-serif;font-size:15px;font-weight:600;color:var(--ink)}
.foot-rule{left:98px;top:3202px;width:1004px;height:1px;background:var(--rule)}
.copy{left:0;top:3230px;width:1200px;text-align:center;font-size:14px;font-weight:700;color:var(--ink)}
</style>
</head>
<body>

<header>
  <div class="abs topbar"></div>
  <svg class="abs tab" width="1200" height="83" aria-hidden="true"><polygon points="458,0 742,0 712,83 488,83" fill="#ffffff"/></svg>
  <nav class="nav left"><a href="#">HOME</a><a href="#">ABOUT US</a><a href="#">SERVICES</a></nav>
  <div class="abs brand brand-top">Corvelle<small>Solutions</small></div>
  <nav class="nav right"><a href="#">WHY US</a><a href="#">BLOG</a><a href="#">CONTACT US</a></nav>
</header>

<section>
  <div class="abs hero"></div>
  <div class="abs hero-art" role="img" aria-label="Tablet with glowing network of connected device icons around a central emblem"></div>
  <h1 class="abs hero-title">Corvelle</h1>
  <p class="abs hero-quote">“Free choices become the matrix of human life”</p>
  <p class="abs hero-sub">An environment in which something develops; a surrounding medium or structure.</p>
  <a class="abs btn btn-amber" style="left:98px;top:418px" href="#">Read More</a>
  <svg class="abs chev" style="left:36px" width="28" height="50" aria-hidden="true"><polyline points="24,3 4,25 24,47" fill="none" stroke="#fff" stroke-width="3"/></svg>
  <svg class="abs chev" style="left:1136px" width="28" height="50" aria-hidden="true"><polyline points="4,3 24,25 4,47" fill="none" stroke="#fff" stroke-width="3"/></svg>
</section>

<section>
  <h2 class="abs welcome-kicker">Welcome To</h2>
  <h2 class="abs welcome-title">Corvelle</h2>
  <p class="abs welcome-copy">Corvelle Solutions is an IT Managed Services Provider (MSP) that has more than 25 years experience growing and collaborating in the IT Industry. Our expertise lies in listening to and understanding our more than 1000 customers’ needs and delivering the best value for money IT Infrastructure and Technology solutions. We believe in loyal and lasting relationships creating a matrix within which your company can grow and outperform it’s own expectations.</p>
  <a class="abs btn btn-amber" style="left:101px;top:997px" href="#">Read More</a>
  <div class="abs frame"></div>
  <div class="abs photo-team" role="img" aria-label="Team working together at a table with laptops and notes, seen from above"></div>
</section>

<section>
  <div class="abs services"></div>
  <h2 class="abs services-title">Our Services</h2>
  <div class="abs rule-w" style="left:546px;top:1310px;width:108px"></div>

  <div class="abs svc" style="left:80px">
    <div class="icon"><svg width="56" height="56" viewBox="0 0 56 56" aria-hidden="true"><circle cx="28" cy="18" r="11" fill="#fff"/><path d="M8 52c0-14 9-20 20-20s20 6 20 20z" fill="#fff"/><path d="M28 34l-3 6 3 10 3-10z" fill="#4b4847"/></svg></div>
    <h3>Managed IT Services</h3><div class="bar"></div>
    <p>Corvelle brings a personal touch to you through our IT consulting services. We collaborate with partners across the globe to bring the best technology to you. You can rely on our expertise to design.</p>
    <a class="btn btn-ghost" href="#">Contact Us Now</a>
  </div>

  <div class="abs svc" style="left:420px">
    <div class="icon hot"><svg width="60" height="56" viewBox="0 0 60 56" aria-hidden="true"><rect x="16" y="14" width="34" height="16" rx="3" transform="rotate(18 33 22)" fill="#fff"/><rect x="20" y="34" width="5" height="14" fill="#fff"/><rect x="12" y="46" width="20" height="4" fill="#fff"/><path d="M6 20a10 10 0 0 1 8-8M2 22a16 16 0 0 1 12-14" fill="none" stroke="#fff" stroke-width="2.5"/></svg></div>
    <h3>Remote Monitoring &amp; Management</h3><div class="bar"></div>
    <p>Corvelle brings you an all-encompassing service that includes managed antivirus, web protection, backup &amp;amp; recovery and email security. You will be able to manage all devices.</p>
    <a class="btn btn-ghost fill" href="#">Contact Us Now</a>
  </div>

  <div class="abs svc" style="left:760px">
    <div class="icon"><svg width="64" height="48" viewBox="0 0 64 48" aria-hidden="true"><path d="M4 26C14 10 50 10 60 26C50 40 14 40 4 26z" fill="none" stroke="#fff" stroke-width="3"/><circle cx="32" cy="26" r="9" fill="#fff"/><path d="M20 8l4 6M32 4v7M44 8l-4 6" stroke="#fff" stroke-width="3"/></svg></div>
    <h3>Virtualisation</h3><div class="bar"></div>
    <p>Corvelle brings you the high performance Hyper Cloud, which reduces your total IT spend in comparison to competitors like Nimbus, Stratocloud and Vaultora.</p>
    <a class="btn btn-ghost" href="#">Contact Us Now</a>
  </div>
</section>

<section>
  <div class="abs why-art" role="img" aria-label="Blue padlock surrounded by circuit and data lines, symbolising security"></div>
  <h2 class="abs why-kicker">Corvelle Solutions</h2>
  <h2 class="abs why-title">Why Choose Us</h2>
  <div class="abs why-copy">
    <p>Corvelle Solutions was founded in 2000 and is in the business of collaborating with partners to bring the best technologies to you.</p>
    <p>We have more than 25 years experience in the IT industry, servicing customers across the GTA and Ontario. Our customers come from different industry sectors including Medical, Financial, Real Estate, Legal and more. We work together with our customers as members of their teams to realize their IT visions and goals.</p>
    <p>We have collaborated with partners across the globe to ensure that we bring the most innovate and functional technology to our customers. We can proudly say that we offer the best Value for Money solutions.</p>
  </div>
  <a class="abs btn btn-amber" style="left:573px;top:2289px" href="#">Read More</a>
</section>

<section>
  <div class="abs eng"></div>
  <div class="abs eng-art" role="img" aria-label="Futuristic holographic interface glowing in soft blue light"></div>
  <div class="abs eng-copy">
    <p>Our engineers are highly skilled and we invest time and money in ensuring they are up to date on the latest technologies so as to better support our customers. We ensure that we are proactive and communicating effectively. In times of crisis, it is not only about resolving the problem, but also about communicating effectively and ensuring that our customers know that we are right there beside them.</p>
    <p>You need a loyal and committed partner like Corvelle who can solve problems and help to ensure that your IT infrastructure is secure and operating beyond expectations for the long term.</p>
  </div>
</section>

<footer>
  <div class="abs brand brand-foot">Corvelle<small>Solutions</small></div>
  <div class="abs social" aria-label="Social links"><span></span><span></span><span></span><span></span><span></span></div>
  <nav class="abs foot-nav"><span>HOME</span><span>|</span><span>ABOUT US</span><span>|</span><span>SERVICES</span><span>|</span><span>WHY US</span><span>|</span><span>BLOG</span><span>|</span><span>CONTACT US</span></nav>
  <div class="abs foot-rule"></div>
  <p class="abs copy">Copyrights @ 2018 Corvelle. All Rights Reserved.</p>
</footer>

</body>
</html>
```